Hispanic Financial Counseling and Advocate Firm seeks business card design

Looking for a clean, professional business card design. This is a firm that specializes in providing financial education, coaching, and planning to the Hispanic community. The name of the company is Valemar, which means to prosper. We need a design that is clean, professional, and invokes trust, professionalism, but also welcoming. Our logo is a plant growing from a hand to give the messaging of of being in control of growing your financial future and security. Its part of a larger organization names Celesta Financial Group, who's logo is a tree with multi colored branches. We have the back of the card designed so we just need the front designed. the back is blue, so front needs to be a different background color, not blue.

Target Market(s)

Hispanic Community looking to better their future

Industry/Entity Type

financial services

Contact Information for Business Card

contact info: Anselmo Ibarra Jr, 951-555-0147, info@celestafinancialgroup.example. Celestafinancialgroup.example. tag line: Para un futuro mas seguro!

Requirements
Must have
• basics: logo, contact info.
Nice to have
• possibly incorporate the tree logo provided somehow
Should not have
• should not look like the back, needs to be different from the back provided.

```html
<!DOCTYPE html>
<html lang="es">
<head>
<meta charset="utf-8">
<title>Valemar – Tarjeta de presentación</title>
<link href="https://fonts.googleapis.com/css2?family=Montserrat:wght@300;400;500;600;700&display=swap" rel="stylesheet">
<style>
  :root {
    --backdrop: #8fad78;
    --navy: #03213d;
    --slate: #3d4b70;
    --green: #5cab2a;
    --paper: #ffffff;
    --ink: #2b3550;
    --leaf-green: #8cc63f;
    --leaf-blue: #1fa9e1;
    --leaf-red: #ef3b3b;
    --leaf-purple: #a98bd4;
    --leaf-yellow: #f6c619;
  }
  * { box-sizing: border-box; margin: 0; padding: 0; }
  html, body { width: 1200px; height: 1056px; overflow: hidden; }
  body {
    background: var(--backdrop);
    font-family: "Montserrat", sans-serif;
    position: relative;
  }
  .card {
    position: absolute;
    width: 640px;
    height: 366px;
    overflow: hidden;
  }

  /* Back of card */
  .card-back { left: 190px; top: 100px; background: var(--navy); color: var(--paper); }
  .parent-brand {
    position: absolute; left: 80px; top: 80px;
    display: flex; align-items: center; gap: 28px;
  }
  .parent-brand .mark {
    width: 118px; height: 118px; border-radius: 50%;
    background: var(--paper); opacity: .9;
  }
  .parent-brand .divider { width: 1px; height: 150px; background: var(--paper); }
  .parent-brand .name { font-weight: 600; line-height: 1; }
  .parent-brand .name-main { display: block; font-size: 78px; letter-spacing: -2px; }
  .parent-brand .name-sub { display: block; font-size: 27px; letter-spacing: 2px; margin-top: 6px; }
  .services {
    position: absolute; left: 120px; top: 262px;
    list-style: none; font-size: 15px; line-height: 1.45; text-align: center; width: 420px;
  }
  .services li { display: inline; white-space: nowrap; margin: 0 4px; }
  .dot { display: inline-block; width: 8px; height: 8px; border-radius: 50%; margin-right: 5px; vertical-align: middle; }
  .dot.green { background: var(--leaf-green); }
  .dot.blue { background: var(--leaf-blue); }
  .dot.red { background: var(--leaf-red); }
  .dot.purple { background: var(--leaf-purple); }
  .dot.yellow { background: var(--leaf-yellow); }

  /* Front of card */
  .card-front { left: 360px; top: 590px; background: var(--paper); color: var(--ink); }
  .brand {
    position: absolute; left: 44px; top: 150px;
    display: flex; align-items: center; gap: 10px;
  }
  .brand .mark { width: 30px; height: 30px; border-radius: 50%; background: var(--green); }
  .brand .name { font-size: 34px; font-weight: 500; color: var(--green); }
  .contact { position: absolute; left: 290px; top: 110px; }
  .contact .person { font-size: 24px; font-weight: 700; color: var(--green); margin-bottom: 14px; }
  .contact ul { list-style: none; }
  .contact li { display: flex; align-items: center; gap: 9px; font-size: 13px; margin-bottom: 9px; }
  .icon {
    width: 18px; height: 18px; border-radius: 3px; background: var(--green);
    display: flex; align-items: center; justify-content: center; flex: none;
  }
  .tagline-band {
    position: absolute; right: 0; top: 286px; width: 400px; height: 30px;
    background: var(--slate); color: var(--paper);
    clip-path: polygon(14px 0, 100% 0, 100% 100%, 0 100%);
    display: flex; align-items: center; justify-content: center;
    font-size: 13px; font-weight: 700; letter-spacing: 2px; text-transform: uppercase;
  }
</style>
</head>
<body>

<section class="card card-back" aria-label="Reverso de la tarjeta">
  <div class="parent-brand">
    <span class="mark" aria-hidden="true"></span>
    <span class="divider" aria-hidden="true"></span>
    <span class="name">
      <span class="name-main">Celesta</span>
      <span class="name-sub">Financial Group Inc</span>
    </span>
  </div>
  <ul class="services">
    <li><span class="dot green"></span>Inmigración</li>
    <li><span class="dot blue"></span>Planificacion Financiera</li>
    <li><span class="dot red"></span>Seguros</li>
    <li><span class="dot purple"></span>Impuestos</li>
    <li><span class="dot red"></span>Y mas</li>
    <li><span class="dot yellow"></span>Preparación de documentos</li>
  </ul>
</section>

<section class="card card-front" aria-label="Frente de la tarjeta">
  <div class="brand">
    <span class="mark" aria-hidden="true"></span>
    <span class="name">Valemar</span>
  </div>
  <div class="contact">
    <p class="person">Anselmo Ibarra Jr</p>
    <ul>
      <li>
        <span class="icon"><svg width="11" height="11" viewBox="0 0 24 24"><path fill="#fff" d="M6.6 10.8a15 15 0 0 0 6.6 6.6l2.2-2.2c.3-.3.7-.4 1-.2 1.1.4 2.3.6 3.6.6.6 0 1 .4 1 1V20c0 .6-.4 1-1 1A17 17 0 0 1 3 4c0-.6.4-1 1-1h3.5c.6 0 1 .4 1 1 0 1.3.2 2.5.6 3.6.1.3 0 .7-.2 1z"/></svg></span>
        951-555-0147
      </li>
      <li>
        <span class="icon"><svg width="12" height="10" viewBox="0 0 24 18"><rect x="1.5" y="1.5" width="21" height="15" fill="none" stroke="#fff" stroke-width="2.5"/><path d="M2 2l10 8 10-8" fill="none" stroke="#fff" stroke-width="2.5"/></svg></span>
        info@celestafinancialgroup.example
      </li>
      <li>
        <span class="icon"><svg width="10" height="11" viewBox="0 0 20 22"><path fill="#fff" d="M2 1l16 9-7 2 4 8-3 1.5-4-8-6 5z"/></svg></span>
        Celestafinancialgroup.example
      </li>
    </ul>
  </div>
  <div class="tagline-band">Para un futuro mas seguro!</div>
</section>

</body>
</html>
```